San Francisco Leading Consulting firm - 47Nova Web Design Project

•Create a Web Design
•Uncoded webpage layout design
•2 Pages Design - Homepage + Interior Page

Task Description
Hello, we're looking for a re-design our current website www.47nova-example.com

we have a sample mockup design @

http://47nova.civicpane-example.org/

This shows the layout that we like and also a sample of 6 pictures that would change based on where you mouse over..

6 pictures HOME design needs to be included.

SMART
THOUGHTFUL
FLEXIBLE
CREATIVE SERVICES
TECHNICAL SERVICES
PARTNERS

sites we like:

http://www.brelmoradvisory-example.com/Home.cfm?id=Home
http://www.pixelquarry-example.com/index.html

Our company can be best described as: 100+ employees, cutting-edge, depandable, innovative, strong, smart.

Our Primary focus is: IT Consulting Services and Creative Design services

47Nova LLC is a consulting firm providing creative design, business and technology solutions to both private and public interests.

Established in 1996, 47Nova is a San Francisco based company providing specialists for a range of business needs including:

Creative Design Services
•Print
•Logo Design
•Website Design
•Illustration

and

Business and Technology solutions

•Application Software and Web Development
•Business Process Re-Design (BPR)
•Business/Systems Analysis and Requirement Documentation
•Mentoring and Training
•Network/Hardware Installation Services
•System Design and Architecture
•Vendor Management
•Teamvault Architecture and Implementation

our sample mockup site:

Reason: Due to holiday season, we're not available to work with designers and finilize our design.  

Thank you very much for submitting your design.

We appreciate your time and creativity.   Since, our office is currently closed for holidays, we will be reviewing it in details next week and will make our decision as soon as possible.

It would be great if you could submit any of your changes by Wed next week, so it would be part of our reviews. 

Please see updated wireframe under attachments:  we have some minor updates to our wireframe that we would like you to update your designs, if possible.  

We also encorouge you not to use our standard wireframe and come up with more unique designs.   Everything would be considered when we review your design.

 

Target Market(s)

Creative services and professional services clients, including government agencies

Industry/Entity Type

Business

Requirements
Must have
• Clean, professional look, easy navigation

```html
<!DOCTYPE html>
<html lang="en">
<head>
<meta charset="utf-8">
<title>47Nova – About us</title>
<link rel="stylesheet" href="https://fonts.googleapis.com/css2?family=Arimo:wght@400;700&display=swap">
<style>
  :root {
    --backdrop: #a3a3a3;
    --page: #ffffff;
    --nav: #7a7a7a;
    --nav-divider: #d8d8d8;
    --accent-red: #d7242b;
    --text: #4a4a4a;
    --tagline: #5a5a5a;
    --band: rgba(70, 70, 70, 0.85);
    --footer-text: #5c5c5c;
    --login: #8a8a8a;
  }
  * { box-sizing: border-box; margin: 0; padding: 0; }
  html, body { width: 1200px; height: 900px; overflow: hidden; }
  body {
    background: var(--backdrop);
    font-family: "Arimo", Arial, sans-serif;
    color: var(--text);
    position: relative;
  }
  .page {
    position: absolute; left: 44px; top: 44px;
    width: 1112px; height: 776px;
    background: var(--page);
    overflow: hidden;
  }
  .brand {
    position: absolute; left: 28px; top: 26px;
    display: flex; align-items: center; gap: 12px;
  }
  .brand-mark { width: 30px; height: 30px; background: var(--accent-red); border-radius: 50%; }
  .brand-name { font-size: 38px; font-weight: 400; color: #3a3a3a; letter-spacing: 1px; }
  .login {
    position: absolute; right: 16px; top: 16px;
    background: var(--login); color: #fff;
    font-size: 13px; font-weight: 700;
    padding: 4px 9px; border-radius: 2px;
  }
  .main-nav {
    position: absolute; left: 20px; top: 118px; width: 1076px; height: 32px;
    background: var(--nav);
    display: flex;
  }
  .main-nav a {
    color: #fff; text-decoration: none; text-transform: uppercase;
    font-size: 16px; line-height: 32px; padding: 0 16px;
    border-right: 2px solid var(--nav-divider);
  }
  .nav-rule { position: absolute; left: 20px; top: 150px; width: 1076px; height: 4px; background: var(--accent-red); }
  .nav-rule-thin { position: absolute; left: 20px; top: 156px; width: 1076px; height: 2px; background: #bdbdbd; }
  .hero {
    position: absolute; left: 20px; top: 160px; width: 1076px; height: 132px;
    background: linear-gradient(90deg, #8fb4d6 0%, #c9d3dc 25%, #a9b0b8 55%, #d5dde5 80%, #9fc3e2 100%);
  }
  .hero-band {
    position: absolute; left: 20px; top: 248px; width: 1076px; height: 44px;
    background: var(--band);
  }
  .hero-band h1 { color: #fff; font-size: 25px; font-weight: 700; line-height: 44px; padding-left: 14px; }
  .intro {
    position: absolute; left: 28px; top: 308px; width: 812px;
    font-size: 15px; line-height: 21px;
  }
  .intro p + p { margin-top: 21px; }
  .expertise {
    position: absolute; left: 28px; top: 478px;
    list-style: none; font-size: 15px; line-height: 20.7px;
  }
  .expertise li { padding-left: 18px; position: relative; }
  .expertise li::before {
    content: ""; position: absolute; left: 0; top: 7px;
    width: 7px; height: 7px; background: var(--accent-red);
  }
  .traits {
    position: absolute; right: 40px; top: 494px;
    text-align: right; font-size: 40px; line-height: 40.5px;
    color: var(--tagline); font-weight: 400;
  }
  .copyright {
    position: absolute; left: 56px; top: 846px;
    font-size: 11px; color: var(--footer-text);
  }
</style>
</head>
<body>
  <div class="page">
    <div class="brand">
      <span class="brand-mark"></span>
      <span class="brand-name">47Nova</span>
    </div>
    <div class="login">Login</div>

    <nav class="main-nav">
      <a href="#">Company</a>
      <a href="#">Technical Services</a>
      <a href="#">Creative Services</a>
      <a href="#">Partners</a>
      <a href="#">Contact Us</a>
    </nav>
    <div class="nav-rule"></div>
    <div class="nav-rule-thin"></div>

    <div class="hero" role="img" aria-label="Photo of modern office towers against a blue sky"></div>
    <div class="hero-band"><h1>About us</h1></div>

    <div class="intro">
      <p>47Nova provides professional experience in all phases of IT projects from vendor selection to post production support. We assist our clients not only in their IT solutions, but also provide professional services such as transitioning with conversion activities, Business Process Reengineering (BPR), training and business support. We have provided vendor analysis and selection, project oversight, architecture, requirements gathering and system certification functions.</p>
      <p>Our corporate consulting services include a wide array of talent and expertise in the following:</p>
    </div>

    <ul class="expertise">
      <li>Analysis</li>
      <li>Business Intelligence</li>
      <li>CRM</li>
      <li>Network/Hardware Installation Services</li>
      <li>Project Management</li>
      <li>Process Redesign</li>
      <li>Production Support</li>
      <li>SQL</li>
      <li>Process Redesign</li>
      <li>System Design and Architecture</li>
      <li>Vendor Management</li>
    </ul>

    <div class="traits">
      100+ employees<br>cutting-edge<br>dependable<br>innovative<br>strong<br>smart
    </div>
  </div>

  <p class="copyright">Copyright 2010, 47Nova, LLC All rights reserved.</p>
</body>
</html>
```